TM Holdings-Homes for Tomorrow's World

TM Holdings is a Residential Real Estate company which specializes in buying and selling homes. We pride ourselves on service, expertise, and building relationships. I would like to do a Billboard Ad for a The Size is 14 feet (Height) x 48 feet (width) displaying our current motto for "Real Estate of the Future" We have launched new programs and working with leaders in our industy Pavrit and other tech companies and changing the way Real Estate is done in Las Vegas, NV. Its exciting and NEW so we want to get the word out. Color Scheme Red, White, Grey and maybe black. Logo is uploaded and so is a picture head shot. I would like to see options with my headshot and with out.

```html
<!DOCTYPE html>
<html lang="en">
<head>
<meta charset="utf-8">
<title>TM Holdings – Billboard</title>
<link rel="stylesheet" href="https://fonts.googleapis.com/css2?family=Oswald:wght@200;400;700&display=swap">
<style>
  :root {
    --backdrop: #eceef1;
    --panel-grey: #3a3c40;
    --stripe-dark: #2b2d30;
    --brand-red: #c8102e;
    --white: #ffffff;
    --photo-sky: #b7c3de;
    --photo-dusk: #9aa3bd;
    --photo-siding: #8a8580;
    --photo-glow: #f0d59c;
    --photo-ground: #4f4c47;
    --portrait-bg: #f6f6f6;
    --portrait-tone: #c9a58c;
    --portrait-suit: #1c2436;
    --portrait-shirt: #2d4f86;
  }
  html, body {
    margin: 0;
    width: 1200px;
    height: 900px;
    overflow: hidden;
    background: var(--backdrop);
  }
  .canvas {
    position: relative;
    width: 1200px;
    height: 900px;
  }
  .billboard {
    position: absolute;
    left: 30px;
    top: 284px;
    width: 1140px;
    height: 332px;
    display: block;
    box-shadow: 0 6px 18px rgba(0,0,0,.18);
  }
  .panel { fill: var(--panel-grey); }
  .stripe-dark { fill: var(--stripe-dark); }
  .stripe-white { fill: var(--white); }
  .portrait-frame { fill: var(--white); }
  .portrait-ring { fill: none; stroke: var(--brand-red); stroke-width: 3; stroke-linecap: round; }
  .logo-plate { fill: var(--white); }
  .brand-name {
    font-family: 'Oswald', sans-serif;
    font-weight: 400;
    font-size: 38px;
    fill: var(--brand-red);
    letter-spacing: 1px;
  }
  .headline-lead {
    font-family: 'Oswald', sans-serif;
    font-weight: 700;
    font-size: 35px;
    fill: var(--white);
  }
  .headline-key {
    font-family: 'Oswald', sans-serif;
    font-weight: 200;
    font-size: 96px;
    fill: var(--white);
    letter-spacing: 2px;
  }
</style>
</head>
<body>
<main class="canvas">
  <svg class="billboard" viewBox="0 0 1030 300" xmlns="http://www.w3.org/2000/svg" aria-label="TM Holdings billboard: Real Estate of the Future">
    <defs>
      <linearGradient id="houseTones" x1="0" y1="0" x2="0" y2="1">
        <stop offset="0" stop-color="var(--photo-sky)"/>
        <stop offset="0.3" stop-color="var(--photo-dusk)"/>
        <stop offset="0.6" stop-color="var(--photo-siding)"/>
        <stop offset="1" stop-color="var(--photo-ground)"/>
      </linearGradient>
      <radialGradient id="houseGlow" cx="0.48" cy="0.72" r="0.45">
        <stop offset="0" stop-color="var(--photo-glow)" stop-opacity="0.9"/>
        <stop offset="1" stop-color="var(--photo-glow)" stop-opacity="0"/>
      </radialGradient>
      <radialGradient id="portraitTones" cx="0.5" cy="0.35" r="0.7">
        <stop offset="0" stop-color="var(--portrait-tone)"/>
        <stop offset="0.35" stop-color="var(--portrait-tone)" stop-opacity="0.6"/>
        <stop offset="0.55" stop-color="var(--portrait-bg)" stop-opacity="0"/>
      </radialGradient>
      <linearGradient id="portraitBase" x1="0" y1="0" x2="0" y2="1">
        <stop offset="0" stop-color="var(--portrait-bg)"/>
        <stop offset="0.6" stop-color="var(--portrait-bg)"/>
        <stop offset="0.72" stop-color="var(--portrait-suit)"/>
        <stop offset="1" stop-color="var(--portrait-suit)"/>
      </linearGradient>
      <clipPath id="houseClip"><polygon points="0,0 612,0 462,300 0,300"/></clipPath>
      <clipPath id="portraitClip"><circle cx="578" cy="160" r="108"/></clipPath>
    </defs>

    <rect class="panel" x="0" y="0" width="1030" height="300"/>

    <g class="house-photo" clip-path="url(#houseClip)" role="img" aria-label="Photo of a lit two-storey family home at dusk">
      <rect x="0" y="0" width="612" height="300" fill="url(#houseTones)"/>
      <rect x="0" y="0" width="612" height="300" fill="url(#houseGlow)"/>
    </g>

    <polygon class="stripe-dark" points="612,0 626,0 476,300 462,300"/>
    <polygon class="stripe-white" points="628,0 642,0 492,300 478,300"/>

    <circle class="portrait-frame" cx="578" cy="160" r="118"/>
    <g class="headshot" clip-path="url(#portraitClip)" role="img" aria-label="Headshot of the agent in a dark blazer and blue shirt">
      <rect x="470" y="52" width="216" height="216" fill="url(#portraitBase)"/>
      <rect x="470" y="52" width="216" height="216" fill="url(#portraitTones)"/>
      <rect x="566" y="218" width="24" height="50" fill="var(--portrait-shirt)"/>
    </g>
    <path class="portrait-ring" d="M578,50 A110,110 0 0 1 578,270"/>

    <path class="logo-plate" d="M712,0 H1010 V58 Q1010,80 988,80 H742 Q712,80 712,52 Z"/>
    <text class="brand-name" x="861" y="56" text-anchor="middle">TM Holdings</text>

    <text class="headline-lead" x="731" y="158">Real Estate of the</text>
    <text class="headline-key" x="728" y="258">FUTURE</text>
  </svg>
</main>
</body>
</html>
```